PixelGuild CEO Needs a Graphic for a Blog About Crowdsourcing and Online Employment

We need a simple graphic / banner for a blog post that's going to be posted on a large publication (like ByteHerald, Marlowe Commerce Quarterly).

The article will be written by Bram Ostiver (PixelGuild's CEO) and the title will be "Why Websites Will Become the Biggest Employers in the World". The article is about why online employers (like PixelGuild and Tasklynx) will one day have more 'workers' than offline employers.

We'd really like to get this ASAP - so early submissions encouraged. We will try and get the winning designer linked to from the article.

Note that this brief is similar to a previous project that we ran http://jobs.pixelguild-example.com/job.aspx?id=58213 where the article and design was published on ByteHerald http://byteherald-example.com/2012/12/08/asias-hidden-gig-surge/ and the designer (Moravia) was linked to from ByteHerald.

Target Market(s)

Entrepreneurs, journalists, small business owners, tech people.

Industry/Entity Type

Business

Requirements
Must have
• The graphic SHOULD have:
1) Have the text "Why Websites Will Become the Biggest Employers in the World" with some nice design and fonts (consider grey subtle pattern background and white drop shadow on fonts) - see attached examples
2) Have the dimensions 640px wide by 240px wide
Nice to have
• The graphic COULD have:

1) Incorporate the following words in the background (like a word cloud): crowdsource, microtask, crowdfund, witkey, outsource, freelance, online, work from home

OR

2) Incorporate logos of new online employers (Tasklynx, vYard, PixelGuild, ChoreFinch, Lunqiaofu, ClockworkPawn, Frameharbor) into the design. If the background of the graphic is grey, ideally, these logos would also be greyscale i.e. they should form a background motif.

OR

3) Show some graphic communicating themes from the article e.g. laptop, globe, workers, connections across the globe

OR

4) Have a second line of text "Why Crowdsourcing Websites Will Overtake Traditional Employers"
Should not have
• Should NOT have:
1) Any photos or clipart

```html
<!DOCTYPE html>
<html lang="en">
<head>
<meta charset="utf-8">
<title>Why Websites Will Become the Biggest Employers in the World</title>
<link rel="stylesheet" href="https://fonts.googleapis.com/css2?family=Roboto+Condensed:wght@300;400;700&family=Roboto:wght@300&display=swap">
<style>
  :root {
    --bg: #a7b3ba;
    --cloud: #b9c3c9;
    --glow: #c9d1d6;
    --ink: #1d4658;
    --light: #ffffff;
  }
  html, body {
    margin: 0;
    padding: 0;
    width: 1200px;
    height: 450px;
    overflow: hidden;
    background: var(--bg);
  }
  .banner {
    display: block;
    width: 1200px;
    height: 450px;
    font-family: "Roboto Condensed", "Arial Narrow", sans-serif;
  }
  .banner-bg { fill: var(--bg); }
  .word-cloud text { fill: var(--cloud); font-weight: 400; }
  .headline-strong { fill: var(--ink); font-weight: 700; }
  .headline-thin { fill: var(--ink); font-weight: 300; }
  .headline-white { fill: var(--light); font-weight: 300; }
  .headline-wide { fill: var(--light); font-weight: 300; font-family: "Roboto", "Helvetica Neue", sans-serif; }
  .subtitle { fill: var(--ink); font-weight: 700; }
</style>
</head>
<body>
<svg class="banner" viewBox="0 0 1200 450" xmlns="http://www.w3.org/2000/svg" role="img"
     aria-label="Why websites will become the biggest employers in the world">
  <defs>
    <filter id="soft-glow" x="-5%" y="-5%" width="110%" height="120%">
      <feDropShadow dx="1" dy="2" stdDeviation="1.5" flood-color="#ffffff" flood-opacity="0.35"/>
    </filter>
    <radialGradient id="ornament-tone">
      <stop offset="0" stop-color="var(--glow)" stop-opacity="0.9"/>
      <stop offset="0.7" stop-color="var(--glow)" stop-opacity="0.55"/>
      <stop offset="1" stop-color="var(--bg)" stop-opacity="0"/>
    </radialGradient>
  </defs>

  <rect class="banner-bg" width="1200" height="450"/>

  <circle class="ornament ornament-right" cx="1050" cy="244" r="230" fill="url(#ornament-tone)"
          role="img" aria-label="Large concentric target rings decoration"/>
  <circle class="ornament ornament-left" cx="37" cy="319" r="90" fill="url(#ornament-tone)"
          role="img" aria-label="Small concentric target rings decoration"/>

  <g class="word-cloud">
    <text x="0" y="24" font-size="24">online</text>
    <text x="200" y="26" font-size="24">crowdsource</text>
    <text x="440" y="22" font-size="22">freelance</text>
    <text x="610" y="26" font-size="24">crowdsource</text>
    <text x="820" y="24" font-size="22">microtask</text>
    <text x="1020" y="24" font-size="24">crowdfund</text>
    <text x="0" y="60" font-size="28">outsource</text>
    <text x="760" y="62" font-size="24">online</text>
    <text x="1010" y="70" font-size="26">freelance</text>
    <text x="760" y="118" font-size="34">work from home</text>
    <text x="40" y="118" font-size="24">work from home</text>
    <text x="0" y="155" font-size="22">witkey</text>
    <text x="1000" y="150" font-size="26">online</text>
    <text x="880" y="200" font-size="26">microtask</text>
    <text x="1060" y="212" font-size="24">witkey</text>
    <text x="880" y="256" font-size="26">crowdsource</text>
    <text x="560" y="330" font-size="24">microtask</text>
    <text x="420" y="330" font-size="24">online</text>
    <text x="120" y="320" font-size="24">outsource</text>
    <text x="1000" y="320" font-size="26">crowdfund</text>
    <text x="980" y="370" font-size="24">witkey</text>
    <text x="40" y="422" font-size="32">crowdsource</text>
    <text x="230" y="440" font-size="26">outsource</text>
    <text x="420" y="424" font-size="26">online</text>
    <text x="990" y="432" font-size="30">work from home</text>
    <text x="540" y="446" font-size="22">freelance</text>
  </g>

  <g class="headline" filter="url(#soft-glow)">
    <text class="headline-white" font-size="44" transform="translate(246 131) rotate(-90)"
          textLength="112" lengthAdjust="spacingAndGlyphs">why</text>
    <text class="headline-strong" x="250" y="131" font-size="112"
          textLength="472" lengthAdjust="spacingAndGlyphs">WEBSITES</text>
    <text class="headline-wide" x="22" y="212" font-size="66"
          textLength="494" lengthAdjust="spacingAndGlyphs">will become the</text>
    <text class="headline-strong" x="22" y="294" font-size="92"
          textLength="293" lengthAdjust="spacingAndGlyphs">BIGGEST</text>
    <text class="headline-thin" x="322" y="294" font-size="92"
          textLength="441" lengthAdjust="spacingAndGlyphs">EMPLOYERS</text>
    <text class="headline-white" font-size="40" transform="translate(804 300) rotate(-90)"
          textLength="131" lengthAdjust="spacingAndGlyphs">in the</text>
    <text class="headline-strong" x="669" y="384" font-size="110"
          textLength="312" lengthAdjust="spacingAndGlyphs">WORLD</text>
  </g>

  <g class="subtitle-block">
    <text class="subtitle" x="141" y="358" font-size="27"
          textLength="393" lengthAdjust="spacingAndGlyphs">Why crowdsourcing websites</text>
    <text class="subtitle" x="178" y="399" font-size="27"
          textLength="469" lengthAdjust="spacingAndGlyphs">will overtake traditional employers.</text>
  </g>
</svg>
</body>
</html>
```